New business! Essential Oils Label for 10 mL Essential Oils Bottles

I need a label design for my new essential oils business. The design should be easily transferable between products. Content should include:
label size W x H 1.25 x 2.875

LAVENDER
Lavandula angustifolia
VOLMIRAâ„¢
100% PURE ESSENTIAL OIL
Net 10 mL
For promotions and additional product information visit fb.com/VolmiraOils
VolmiraOils.com
Marlow Bay, FL 33871
888-555-KIPO (5476)
Indications: Massage (10 drops of carrier oil for every drop of essential oil), Bath (10 drops of essential oil) or Inhalation (2-4 drops essential of on a tissue).
EXTERNAL USE ONLY- DILUTE BEFORE APPLICATION
Caution: Do not ingest the oil. Sensitive skin may be irritated by topical use. Avoid contact with eyes. Consult your healthcare practitioner before use. Store oil away from children and pets. Not meant for use during pregnancy. Seek medical care immediately if adverse reaction is experienced.

Target Market(s)

ONLINE SHOPPERS

Industry/Entity Type

Business

Font styles to use
Serif
Sans Serif

Colors

Designer to choose colors to be used in the design.

Requirements
Must have
• CONTENT AS LISTED IN PROJECT DESCRIPTION, LOGO (ATTACHED)
Nice to have
• Files with easily transferable content so the same label design can be used for multiple products.
Should not have
• Too small of print, difficult to read

```html
<!DOCTYPE html>
<html lang="en">
<head>
<meta charset="utf-8">
<title>Volmira Lavender Essential Oil Label</title>
<link rel="stylesheet" href="https://fonts.googleapis.com/css2?family=Montserrat:wght@300;400;500;600&family=Open+Sans:wght@400;600;700&display=swap">
<style>
  :root {
    --bg: #ececec;
    --paper: #ffffff;
    --paper-shade: #e4e4e6;
    --plum: #7b2d6b;
    --silver: #c9c9cc;
    --silver-dark: #8e8e93;
    --pill: #bdbdc1;
    --ink: #2c2c2e;
    --ink-soft: #4a4a4e;
    --white: #ffffff;
  }
  * { box-sizing: border-box; margin: 0; padding: 0; }
  html, body { width: 1200px; height: 900px; overflow: hidden; background: var(--bg); }
  .canvas {
    width: 1200px; height: 900px;
    display: flex; align-items: center; justify-content: center;
  }
  .label {
    display: flex;
    width: 840px; height: 644px;
    box-shadow: 0 14px 40px rgba(0,0,0,0.12);
  }
  .panel {
    position: relative;
    width: 280px; height: 100%;
    background: linear-gradient(180deg, var(--paper) 0%, var(--paper) 48%, var(--paper-shade) 62%);
    overflow: hidden;
  }
  .panel + .panel { border-left: 1px solid #dcdcde; }
  .band {
    position: absolute; left: 0; right: 0; bottom: 0; height: 236px;
    background: var(--plum);
  }
  .band::before {
    content: ""; position: absolute; left: 0; right: 0; top: -14px; height: 14px;
    background: linear-gradient(180deg, var(--silver-dark), var(--silver) 40%, #f2f2f3 60%, var(--silver));
  }
  .info {
    position: absolute; left: 22px; right: 22px; top: 30px;
    font-family: "Open Sans", sans-serif; font-size: 11.5px; line-height: 1.45; color: var(--ink-soft);
  }
  .info p + p { margin-top: 12px; }
  .info b { color: var(--ink); font-weight: 700; }
  .info .warning { font-weight: 600; text-transform: uppercase; color: var(--ink); }
  .contact {
    position: absolute; left: 22px; right: 22px; bottom: 34px;
    font-family: "Open Sans", sans-serif; font-size: 12px; line-height: 1.55; color: var(--white);
  }
  .contact .site { font-weight: 600; margin-top: 8px; }
  .net-side {
    position: absolute; left: 22px; top: 60px;
    font-family: "Montserrat", sans-serif; font-size: 15px; color: var(--plum);
  }
  .brand {
    position: absolute; top: 64px; left: 0; right: 0; text-align: center;
    font-family: "Montserrat", sans-serif; font-weight: 400; font-size: 34px; letter-spacing: 1px; color: var(--ink);
  }
  .brand sup { font-size: 11px; vertical-align: top; margin-left: 2px; }
  .brand-dot {
    display: inline-block; width: 8px; height: 8px; border-radius: 50%;
    background: var(--plum); margin-right: 8px; vertical-align: middle;
  }
  .product {
    position: absolute; top: 290px; left: 0; right: 0; text-align: center;
  }
  .product-name {
    font-family: "Montserrat", sans-serif; font-weight: 500; font-size: 33px; letter-spacing: 6px; color: var(--plum);
  }
  .product-latin {
    font-family: "Open Sans", sans-serif; font-size: 14px; color: var(--ink-soft); margin-top: 4px;
  }
  .claim {
    position: absolute; left: 0; right: 0; bottom: 80px; text-align: center; color: var(--white);
    font-family: "Montserrat", sans-serif;
  }
  .claim-pure { font-size: 26px; font-weight: 400; }
  .claim-type { font-family: "Open Sans", sans-serif; font-size: 16px; font-weight: 600; letter-spacing: 4px; margin-top: 6px; }
  .net {
    position: absolute; left: 0; right: 0; bottom: 26px; text-align: center;
    font-family: "Montserrat", sans-serif; font-size: 15px; color: var(--white);
  }
</style>
</head>
<body>
<main class="canvas">
  <section class="label" aria-label="Lavender essential oil label">
    <div class="panel panel-directions">
      <div class="info">
        <p><b>Indications:</b> Massage (10 drops of carrier oil for every drop of essential oil), Bath (10 drops of essential oil) or Inhalation (2-4 drops essential oil on a tissue).</p>
        <p class="warning">External use only - dilute before application</p>
        <p><b>Caution:</b> Do not ingest the oil. Sensitive skin may be irritated by topical use. Avoid contact with eyes. Consult your healthcare practitioner before use. Store oil away from children and pets. Not meant for use during pregnancy. Seek medical care immediately if adverse reaction is experienced.</p>
      </div>
      <div class="band"></div>
    </div>

    <div class="panel panel-front">
      <div class="brand"><span class="brand-dot"></span>VOLMIRA<sup>™</sup></div>
      <div class="product">
        <div class="product-name">LAVENDER</div>
        <div class="product-latin">Lavandula angustifolia</div>
      </div>
      <div class="band"></div>
      <div class="claim">
        <div class="claim-pure">100% PURE</div>
        <div class="claim-type">ESSENTIAL OIL</div>
      </div>
      <div class="net">0.33 fl. Oz (10 ml)</div>
    </div>

    <div class="panel panel-contact">
      <div class="net-side">Net 10 mL</div>
      <div class="band"></div>
      <div class="contact">
        <p>For promotions and additional product information visit fb.com/VolmiraOils</p>
        <p class="site">VolmiraOils.com</p>
        <p>Marlow Bay, FL 33871</p>
        <p>888-555-KIPO (5476)</p>
      </div>
    </div>
  </section>
</main>
</body>
</html>
```